HARBOR LANTERN COLLECTIVE

Design a website for a membership based organization focusing on entrepreneurship, women's issues and global news regarding commerce.
Also, want a news daily tie in to site, and social media outlets.
I want the colors in strong blue, deep or metallic gold and cream/white like logo which will be provided. I want logo altered with globe to replace small sphere in the design.
Also, board members page that should be redesigned. Might need extra coding.
PLEASE SEE http://harborlanterncollective.example DIDN'T LIKE THIS LAY OUT AT ALL TOO MUCH WHITE AND NOT ENOUGH IMPACT. WANT TO DRAW MEMBERS.

PLEASE SEE http://www.qrtv-example.net/Index.cfm BUT THIS IS WAY TO BUSY BUT I LIKE THE SLIDING.

SEE OUR TWITTER ACCOUNT FOR INSIGHT. @HARBORLANTCOL

Reason: Happy Holidays. The board approving the design will be out on season time vacation until Jan. 2. Please make any edits requested from designer already submitting layouts. Thank you, Delphine

Target Market(s)

GLOBAL BUSINESS WOMEN AND ENTREPRENEURS AGES 20-65

Industry/Entity Type

Media

Number of Pages Required

4 page

Font styles to use
Other font styles liked:
• Baskerville or something similar

Colors
fbed22
3377b5
9bcb3c

Requirements
Must have
• Show diversity of ethnicities if using stock photos. Vibrant and inviting site, MUST JOIN or Be part of this organization. Luxury style
• THIS IS A FOR PROFIT WEBSITE.
• Membership Fees:
• Annual Fee $250
• For an additional fee of $150 you can grow your visibility and voice through our Harbor Lantern Collective Newsletter and Speaker's Bureau (HLCNSB).
• HLC Speaker's Bureau will support your personal, business and organizations' objectives and to give you greater visibility and voice as an authority world leader or business visionary in your field of service.
• HLCSB realizes that so many worthy leaders' in diverse fields of service are never allowed to be heard. If you feel you are a dynamic speaker, run a worthwhile business or organization and whose wisdom and success can be of service of others sign up today and be part of the HLCSB!
• Student Membership
• Discounted student memberships are also available. Students have access to selected group forums, as well as selected groups of members that provide mentoring. Mentoring helps continue the member's legacy and creates a well spring of future leaders. Student membership fees cost just $75 a year.
• Contact us to help promote you and other women's vision throughout the world.
• Join HLC Now!
• CAN YOU PROVIDE A HEADLINE WITHOUT WOMEN SEE TWITTER ACCOUNT.
Nice to have
• Nice headline and well position tabs.
• Home
• Join HLC Now
• Memberships
• HLC Team Leadership
• About Us
• Contact
• HLC is an Effective Women's Initiative for You!
• New Member - Women's Organization
• 20% Discount- Offer Valid on Your Membership Fee When You Join before 1/30/2105
• Memberships
• HLC Leadership
• At Harbor Lantern Collective, we offer the opportunity to connect with women throughout the globe. Join these trailblazers to shorten your path to success and camaraderie.
• Who We Are
• Harbor Lantern Collective is an online women's initiative that promotes your business and visions through social engagement. We are here to help you form strategic partnerships with like-minded women around the world. End your solo journey by becoming a member of HLC.
• HLC also features a forum to promote the services, campaigns, and social activism by our members.
• HLC is about women helping other women. Contact us for more information.
• Learn More about Harbor Lantern Collective
• Contact us for more information in regards to HLC membership and how to get involved.
• SHARE THIS PAGE:
• twitter, fb, instagram, etc.

```html
<!DOCTYPE html>
<html lang="en">
<head>
<meta charset="utf-8">
<title>Harbor Lantern Collective</title>
<link href="https://fonts.googleapis.com/css2?family=Bitter:wght@400;700&family=Lato:wght@400;700&family=Oswald:wght@400&display=swap" rel="stylesheet">
<style>
:root{
  --cream:#fdf4ee;
  --peach:#fde8da;
  --blue:#0b55a8;
  --blue-dark:#083f86;
  --gold:#f6b40e;
  --gold-light:#fcc21f;
  --charcoal:#2f2f2f;
  --text:#333;
  --muted:#555;
  --line:#d9cfc8;
}
*{box-sizing:border-box;margin:0;padding:0}
html,body{width:671px;height:1200px;overflow:hidden}
body{background:var(--cream);font-family:'Lato',sans-serif;color:var(--text);position:relative}
.abs{position:absolute}

/* header */
.brand{left:74px;top:56px;width:140px;font-family:'Lato',sans-serif;font-weight:700;font-size:13px;line-height:15px;color:var(--blue-dark);display:flex;align-items:center;gap:7px}
.brand-dot{flex:none;width:14px;height:14px;border-radius:50%;background:var(--gold)}
.callus{right:160px;top:11px;font-size:12px;color:#444;display:flex;align-items:center;gap:4px;white-space:nowrap}
.callus b{color:var(--blue);font-weight:700;font-size:13px}
.social{display:flex;gap:4px}
.social span{width:18px;height:18px;border-radius:50%;display:block}
.s1{background:#3b5998}.s2{background:#29a9e0}.s3{background:#0e76a8}.s4{background:#e0782b}
.top-social{left:517px;top:9px}
.top-btn{top:37px;height:18px;background:var(--gold);color:#fff;font-size:10px;display:flex;align-items:center;justify-content:center}
.main-nav{left:224px;top:63px;width:447px;height:28px;background:var(--blue);border-radius:6px 0 0 6px;display:flex;align-items:center;padding-left:18px;gap:31px}
.main-nav a{color:#fff;text-decoration:none;font-size:10px;white-space:nowrap}

/* hero */
.hero{left:0;top:101px;width:671px;height:221px}
.deal{left:20px;top:214px;width:220px;text-align:center;color:#333}
.deal h2{font-family:'Bitter',serif;font-weight:400;font-size:21px}
.deal p{font-family:'Bitter',serif;font-size:9.5px;line-height:13px;margin-top:5px}
.btn-white{left:78px;top:278px;width:98px;height:25px;background:#fff;border-radius:3px;box-shadow:0 1px 3px rgba(0,0,0,.25);font-family:'Oswald',sans-serif;font-size:12px;color:#333;display:flex;align-items:center;justify-content:center}
.hero-title{left:288px;top:211px;width:260px;color:#fff;font-family:'Bitter',serif;font-size:15px;line-height:21px;text-shadow:0 1px 2px rgba(0,0,0,.25)}
.hero-title b{font-size:24px;font-weight:400}
.btn-blue{left:288px;top:277px;width:98px;height:26px;background:var(--blue-dark);border-radius:3px;color:#fff;font-family:'Oswald',sans-serif;font-size:12px;display:flex;align-items:center;justify-content:center}

/* features */
.arrow-box{top:375px;width:18px;height:18px;border:1px solid #aaa;background:#fff;display:flex;align-items:center;justify-content:center}
.feature{top:348px;width:163px;height:70px;color:#fff;display:flex;padding:8px 8px;gap:8px;box-shadow:0 2px 3px rgba(0,0,0,.2)}
.feature svg{flex:none}
.feature h3{font-size:9px;font-weight:700;line-height:11px}
.feature p{font-size:8px;line-height:10px;margin-top:3px}
.f-blue{left:73px;background:var(--blue)}
.f-gold{left:254px;background:var(--gold)}
.f-dark{left:435px;background:var(--charcoal)}
.rule{left:100px;top:446px;width:470px;height:1px;background:var(--line)}

/* welcome */
.welcome{left:74px;top:478px;width:296px}
.welcome h2{font-family:'Bitter',serif;font-weight:400;font-size:14px;color:#333}
.welcome h2 span{color:var(--blue)}
.welcome hr{border:0;border-top:1px solid var(--line);margin:4px 0 6px}
.welcome p{font-size:7.8px;line-height:12.6px;color:var(--muted)}
.video{left:390px;top:474px;width:207px;height:119px;background:linear-gradient(135deg,#4a4a4a,#1c1c1c 60%,#3a3a3a);border:3px solid #2b2b2b}
.play{left:87px;top:43px;width:28px;height:28px;border-radius:50%;background:rgba(255,255,255,.55)}

/* student */
.band{left:0;top:621px;width:671px;height:180px;background:var(--peach)}
.star{width:30px;height:30px;border-radius:50%;background:var(--cream);display:flex;align-items:center;justify-content:center;left:320px}
.student-photo{left:74px;top:650px;width:236px;height:95px;border:3px solid #fff;border-radius:4px;background:linear-gradient(120deg,#7a5238,#c9a184 35%,#e5dbd0 55%,#8a7a70);box-shadow:0 1px 3px rgba(0,0,0,.2)}
.student{left:333px;top:646px;width:264px}
.student h2{font-family:'Bitter',serif;font-weight:400;font-size:14px;color:#333}
.student h2 span{color:var(--blue)}
.student hr{border:0;border-top:1px solid var(--line);margin:4px 0 6px}
.student p{font-size:8px;line-height:12.6px;color:var(--muted)}
.student p b{color:var(--blue);font-size:11px}
.btn-gold{left:331px;top:752px;width:86px;height:22px;background:var(--gold);border-radius:2px;font-family:'Oswald',sans-serif;font-size:11px;color:#333;display:flex;align-items:center;justify-content:center}

/* team */
.team-title{left:0;top:825px;width:671px;text-align:center;font-family:'Bitter',serif;font-weight:400;font-size:14px;color:#333}
.team-title span{color:var(--blue)}
.team-rule{left:74px;top:846px;width:523px;height:1px;background:var(--line)}
.member{top:872px;width:117px;height:110px;border:3px solid #fff;box-shadow:0 1px 4px rgba(0,0,0,.25)}
.member-name{top:992px;width:130px;text-align:center;font-size:9.5px;color:#333}

/* footer */
.footer-shape{left:0;top:980px;width:671px;height:220px}
.f-col h4{font-size:9.5px;color:#fff;font-weight:700}
.f-col hr{border:0;border-top:1px solid rgba(255,255,255,.3);margin:4px 0 8px}
.links{list-style:none}
.links li{font-size:7.5px;color:#fff;line-height:15px}
.links li::before{content:"›";margin-right:5px}
.f-col p{font-size:7.5px;color:#fff;line-height:10px}
.email-field{width:116px;height:15px;background:#fff;border-radius:2px;font-size:7px;color:#333;padding:3px 4px;margin-top:8px}
.subscribe{margin-top:10px;width:64px;height:16px;background:var(--gold);border-radius:2px;font-size:8px;color:#333;font-weight:700;display:flex;align-items:center;justify-content:center}
.c-row{display:flex;gap:8px;margin-bottom:12px;align-items:flex-start}
.c-row svg{flex:none;margin-top:1px}
.f-divider{top:1082px;width:1px;height:102px;background:rgba(255,255,255,.2)}
.copy{left:470px;top:1154px;width:127px;text-align:center;font-size:7.5px;color:#fff}
.bottom-social{left:499px;top:1173px}
</style>
</head>
<body>

<!-- header -->
<div class="abs brand"><span class="brand-dot"></span><span>Harbor Lantern Collective</span></div>
<div class="abs callus">
  <svg width="11" height="11" viewBox="0 0 24 24"><path fill="#555" d="M6.6 10.8a15 15 0 0 0 6.6 6.6l2.2-2.2a1 1 0 0 1 1-.25 11.4 11.4 0 0 0 3.6.6 1 1 0 0 1 1 1V20a1 1 0 0 1-1 1A17 17 0 0 1 3 4a1 1 0 0 1 1-1h3.5a1 1 0 0 1 1 1c0 1.25.2 2.45.6 3.6a1 1 0 0 1-.25 1z"/></svg>
  Call Us <b>555-019-4782</b>
</div>
<div class="abs social top-social" role="img" aria-label="Social network links"><span class="s1"></span><span class="s2"></span><span class="s3"></span><span class="s4"></span></div>
<div class="abs top-btn" style="left:472px;width:60px">About Us</div>
<div class="abs top-btn" style="left:538px;width:59px">Contact Us</div>
<nav class="abs main-nav"><a>HOME</a><a>JOIN HLC NOW</a><a>MEMBERSHIPS</a><a>HLC TEAM LEADERSHIP</a></nav>

<!-- hero -->
<svg class="abs hero" viewBox="0 0 671 221">
  <defs>
    <linearGradient id="heroPhoto" x1="0" y1="0" x2="1" y2="1">
      <stop offset="0" stop-color="#b7a58c"/><stop offset=".4" stop-color="#e3c9ae"/><stop offset=".75" stop-color="#c9b898"/><stop offset="1" stop-color="#e9e4dc"/>
    </linearGradient>
    <linearGradient id="heroGold" x1="0" y1="0" x2="1" y2="0">
      <stop offset="0" stop-color="#fcc21f"/><stop offset="1" stop-color="#f7b512"/>
    </linearGradient>
  </defs>
  <rect width="671" height="221" fill="url(#heroPhoto)" role="img" aria-label="Photo of four smiling women of different ages"/>
  <path d="M0 0H205C190 40 215 70 250 100C285 130 270 190 270 221H0Z" fill="url(#heroGold)"/>
  <path d="M205 0C190 40 215 70 250 100C285 130 270 190 270 221" fill="none" stroke="#fff" stroke-width="5"/>
</svg>
<div class="abs deal"><h2>20% Discount</h2><p>Offer Valid on Your Membership Fee<br>When You Join before 1/30/2015</p></div>
<div class="abs btn-white">MEMBERSHIPS</div>
<div class="abs hero-title"><b>HLC</b> is an Effective Women's Initiative for You!</div>
<div class="abs btn-blue">JOIN HLC NOW</div>

<!-- features -->
<div class="abs arrow-box" style="left:34px"><svg width="6" height="9" viewBox="0 0 6 9"><path d="M5 1L1 4.5 5 8" stroke="#666" fill="none" stroke-width="1.4"/></svg></div>
<div class="abs arrow-box" style="left:618px"><svg width="6" height="9" viewBox="0 0 6 9"><path d="M1 1l4 3.5L1 8" stroke="#666" fill="none" stroke-width="1.4"/></svg></div>
<div class="abs feature f-blue">
  <svg width="32" height="30" viewBox="0 0 32 30"><path d="M16 14C10 9 8 6 10 3.5s5-1 6 1c1-2 4-3.5 6-1s0 5.5-6 10.5z" fill="#fff"/><path d="M2 16c3 0 6 4 9 7h10c2 0 2 3 0 3H10M30 16c-3 0-6 4-9 7" fill="none" stroke="#fff" stroke-width="2"/></svg>
  <div><h3>Health and<br>Sanitation</h3><p>rom girlhood to womanhood, females in many societies are fed last and least [...]</p></div>
</div>
<div class="abs feature f-gold">
  <svg width="32" height="24" viewBox="0 0 32 24"><path d="M16 2L31 9 16 16 1 9z" fill="#fff"/><path d="M8 12v6c4 3 12 3 16 0v-6l-8 4z" fill="#fff"/><path d="M29 10v8" stroke="#fff" stroke-width="1.5"/></svg>
  <div><h3>Women<br>Education</h3><p>While the "gender gap" in education has narrowed over the last decade [...]</p></div>
</div>
<div class="abs feature f-dark">
  <svg width="30" height="26" viewBox="0 0 30 26"><path d="M2 24h26" stroke="#fff" stroke-width="2"/><rect x="4" y="12" width="4" height="10" fill="none" stroke="#fff" stroke-width="1.5"/><rect x="11" y="7" width="4" height="15" fill="none" stroke="#fff" stroke-width="1.5"/><rect x="18" y="2" width="4" height="20" fill="none" stroke="#fff" stroke-width="1.5"/></svg>
  <div><h3>Economics and Workforce Development</h3><p>While women's employment has increased in the last two decades around the world [...]</p></div>
</div>
<div class="abs rule"></div>

<!-- welcome -->
<section class="abs welcome">
  <h2>Welcome to <span>Harbor Lantern Collective</span></h2>
  <hr>
  <p>The Harbor Lantern Collective (HLC) is a woman-owned business advisory &amp; consulting organization committed to advancing the economic and political empowerment of women around the world by identifying, exploring and supporting the implementation of profit generating approaches, including business friendly and pro-woman policies. The collective experience of HLC leadership represents a broad knowledge, understanding and high-level expertise in international and local business development [...]</p>
</section>
<div class="abs video" role="img" aria-label="Video still of hands holding a small globe">
  <div class="abs play"></div>
  <svg class="abs" style="left:98px;top:51px" width="10" height="12" viewBox="0 0 10 12"><path d="M0 0l10 6-10 6z" fill="#333"/></svg>
</div>

<!-- student -->
<div class="abs band"></div>
<div class="abs star" style="top:608px"><svg width="18" height="18" viewBox="0 0 20 20"><path d="M10 0l2 8 8 2-8 2-2 8-2-8-8-2 8-2z" fill="var(--gold)"/></svg></div>
<div class="abs student-photo" role="img" aria-label="Photo of a smiling student in a study group"></div>
<section class="abs student">
  <h2>Student <span>Membership</span></h2>
  <hr>
  <p>Discounted student memberships are also available. Students have access to selected group forums, as well as selected groups of members that provide mentoring. Mentoring helps continue the member's legacy and creates a well spring of future leaders. Student membership fees cost just <b>$75</b> a year.</p>
</section>
<div class="abs btn-gold">JOIN HLC NOW</div>
<div class="abs star" style="top:788px"><svg width="18" height="18" viewBox="0 0 20 20"><path d="M10 0l2 8 8 2-8 2-2 8-2-8-8-2 8-2z" fill="var(--gold)"/></svg></div>

<!-- team -->
<h2 class="abs team-title">HLC <span>TEAM</span></h2>
<div class="abs team-rule"></div>
<div class="abs member" style="left:74px;background:linear-gradient(160deg,#dfe3e6,#b03a8f 65%,#333)" role="img" aria-label="Portrait of team member in a magenta blouse"></div>
<div class="abs member" style="left:209px;background:linear-gradient(160deg,#cfe0ea,#e3c4a8 45%,#f2f2f2)" role="img" aria-label="Portrait of team member in a white shirt"></div>
<div class="abs member" style="left:345px;background:linear-gradient(160deg,#6b4b36,#dcb89a 45%,#1f6f86)" role="img" aria-label="Portrait of team member in a teal top"></div>
<div class="abs member" style="left:480px;background:linear-gradient(160deg,#a9956f,#d8b296 45%,#2a2a2a)" role="img" aria-label="Portrait of team member in a dark jacket"></div>
<div class="abs member-name" style="left:68px">Consectetuer Euismod</div>
<div class="abs member-name" style="left:203px">Ullamcorper Suscipit</div>
<div class="abs member-name" style="left:339px">Autem Dolleum</div>
<div class="abs member-name" style="left:474px">Vulputate Velit</div>

<!-- footer -->
<svg class="abs footer-shape" viewBox="0 0 671 220">
  <path d="M0 60C150 25 330 40 450 60C540 75 620 40 671 5V50C610 80 540 90 450 80Z" fill="var(--gold)"/>
  <path d="M0 60C150 25 330 40 450 65C540 85 620 60 671 35V220H0Z" fill="var(--blue)"/>
</svg>

<div class="abs f-col" style="left:74px;top:1082px;width:80px">
  <h4>Quick Links</h4><hr>
  <ul class="links"><li>Home</li><li>Join Hlc Now</li><li>Memberships</li><li>Hlc Team Leadership</li><li>About Us</li><li>Contact</li></ul>
</div>
<div class="abs f-divider" style="left:162px"></div>
<div class="abs f-col" style="left:174px;top:1082px;width:124px">
  <h4>Newsletter Signup</h4><hr>
  <p>Get latest updates by entering your email address</p>
  <div class="email-field">Email Address</div>
  <div class="subscribe">SUBSCRIBE</div>
</div>
<div class="abs f-divider" style="left:308px"></div>
<div class="abs f-col" style="left:321px;top:1082px;width:140px">
  <h4>Contact Information</h4><hr>
  <div class="c-row"><svg width="7" height="10" viewBox="0 0 7 10"><path d="M3.5 0A3.5 3.5 0 0 0 0 3.5C0 6 3.5 10 3.5 10S7 6 7 3.5A3.5 3.5 0 0 0 3.5 0zm0 5a1.5 1.5 0 1 1 0-3 1.5 1.5 0 0 1 0 3z" fill="#fff"/></svg><p>Lorem ipsum dolor sit consectetuer adipiscing elit, diam nonummy nibh Street No 5, zip Code: 897410</p></div>
  <div class="c-row"><svg width="8" height="8" viewBox="0 0 24 24"><path fill="#fff" d="M6.6 10.8a15 15 0 0 0 6.6 6.6l2.2-2.2a1 1 0 0 1 1-.25 11.4 11.4 0 0 0 3.6.6 1 1 0 0 1 1 1V20a1 1 0 0 1-1 1A17 17 0 0 1 3 4a1 1 0 0 1 1-1h3.5a1 1 0 0 1 1 1c0 1.25.2 2.450.6 3.6a1 1 0 0 1-.25 1z"/></svg><p>555-019-4782</p></div>
  <div class="c-row"><svg width="9" height="7" viewBox="0 0 9 7"><rect width="9" height="7" fill="#fff"/><path d="M0 0l4.5 4L9 0" stroke="var(--blue)" fill="none"/></svg><p>info@harborlantern.example</p></div>
</div>
<div class="abs f-divider" style="left:466px"></div>
<div class="abs copy">© 2014 Harbor Lantern Collective.</div>
<div class="abs social bottom-social" role="img" aria-label="Social network links"><span class="s1"></span><span class="s2"></span><span class="s3"></span><span class="s4"></span></div>

</body>
</html>
```